KBR Anti-Money Laundering Postcard

We are a U.S. based regulatory compliance consulting company who services the financial industry (stock, bonds, equities, banking, etc.)

One of the services that we offer is Independent Anti-Money Laundering audit reviews. These reviews are required by U.S. law for certain financial institutions.

We are looking for a 6" x 8.5" horizontally oriented postcard to market our services in this business. The card should be sharp and professional.

The font and back of the card must have our logo and include

"Anti-Money Laundering Compliance" or "Anti-Money Laundering Compliance Services"

We would like the following message to be included on the card either on the front or preferably the back:

"Pellridge & Associates are specialists in Anti-Money Laundering compliance. Our firm’s Anti-Money Laundering compliance solutions include:

• Independent Money Laundering Audits
• Anti-Money Laundering Compliance Procedures
• Anti-Money Laundering Training

Let our expert compliance team assist you in ensuring that your firm is compliant with all of its money laundering and other compliance obligations.

The back of the card should have our address, website, phone number and website: The address is normally included in the return address section noted in the Post Office requirements section blow.

42 W. Halvern Street, Suite 300
Pasadena, CA 91101
(877) 318-4027
info@pellridgeandassociates.example
www.pellridgeandassociates.example

Back of the postcard Post Office Design requirements:

http://www.quillcardprint.example/products/postcard-deluxe

Target Market(s)

Stock Brokerage Firms, Investment Advisers, Banks and other financial institutions

Industry/Entity Type

Financial Planning

Font styles to use
Sans Serif

Requirements
Must have
• Our Logo on the front and back. Clean and professional. Nice artwork.

```html
<!DOCTYPE html>
<html lang="en">
<head>
<meta charset="utf-8">
<title>Pellridge &amp; Associates – Anti-Money Laundering Postcard</title>
<link href="https://fonts.googleapis.com/css2?family=Arimo:wght@400;700&display=swap" rel="stylesheet">
<style>
  :root {
    --bg: #2a2a2a;
    --paper: #ffffff;
    --brand-red: #b3131b;
    --ink: #4a4a4a;
    --ink-dark: #2e2e2e;
    --panel-grey: #6d6e70;
    --line-grey: #555555;
    --night-1: #1f2327;
    --night-2: #4a5158;
    --wine: #3a0c0e;
    --wine-light: #7a1a1d;
    --chart-blue: #3a55c4;
    --chart-deep: #16246b;
    --ring: #9a9c9f;
  }
  * { box-sizing: border-box; margin: 0; padding: 0; }
  html, body { width: 1200px; height: 1000px; overflow: hidden; }
  body {
    background: var(--bg);
    font-family: "Arimo", Arial, sans-serif;
    position: relative;
  }
  .postcard {
    position: absolute;
    left: 290px;
    width: 620px;
    height: 438px;
    background: var(--paper);
    overflow: hidden;
    box-shadow: 0 12px 30px rgba(0,0,0,.55);
  }
  .postcard--back { top: 40px; }
  .postcard--front { top: 522px; }

  .brand {
    position: absolute;
    display: flex;
    align-items: center;
    gap: 8px;
    font-weight: 700;
    letter-spacing: .5px;
    text-transform: uppercase;
  }
  .brand__mark { width: 22px; height: 22px; background: var(--brand-red); }
  .brand--back { left: 36px; top: 36px; font-size: 19px; color: var(--ink-dark); }
  .brand--front { left: 42px; top: 36px; font-size: 19px; color: #ffffff; }

  .intro {
    position: absolute; left: 36px; top: 86px; width: 330px;
    color: var(--brand-red); font-weight: 700; font-size: 12.5px; line-height: 1.35;
  }
  .services {
    position: absolute; left: 44px; top: 148px; list-style: none;
    color: var(--ink); font-size: 12.5px; line-height: 1.4;
  }
  .services li::before { content: "•"; color: var(--brand-red); margin-right: 6px; }
  .assist-panel {
    position: absolute; left: 36px; top: 222px; width: 326px;
    background: var(--panel-grey); color: #fff;
    font-size: 11.5px; line-height: 1.35; padding: 8px 12px; text-align: center;
  }
  .contact { position: absolute; color: var(--ink); font-size: 12.5px; line-height: 1.35; }
  .contact__row { display: flex; gap: 7px; align-items: flex-start; }
  .contact__icon { flex: none; width: 10px; height: 10px; margin-top: 3px; }
  .contact__gap { height: 10px; }
  .contact--back { left: 40px; top: 306px; }
  .contact--front { left: 50px; top: 330px; }

  .stamp-box {
    position: absolute; right: 44px; top: 32px; width: 94px; height: 86px;
    border: 1px solid var(--line-grey);
  }
  .address-lines { position: absolute; left: 400px; top: 150px; width: 180px; }
  .address-lines span { display: block; height: 1px; background: var(--line-grey); margin-bottom: 38px; }

  .front-art { position: absolute; inset: 0; }
  .front-copy { position: absolute; left: 40px; top: 82px; width: 290px; color: #fff; text-align: center; }
  .front-copy h1 {
    font-size: 22px; font-weight: 700; line-height: 1.15; text-transform: uppercase;
  }
  .front-copy p { margin-top: 14px; font-size: 12px; line-height: 1.4; }
</style>
</head>
<body>

<section class="postcard postcard--back" aria-label="Postcard back">
  <div class="brand brand--back"><span class="brand__mark"></span>Pellridge &amp; Associates</div>
  <p class="intro">Pellridge &amp; Associates are specialists in Anti-Money Laundering compliance. Our firm’s Anti-Money Laundering compliance solutions include:</p>
  <ul class="services">
    <li>Independent Money Laundering Audits</li>
    <li>Anti-Money Laundering Compliance Procedures</li>
    <li>Anti-Money Laundering Training</li>
  </ul>
  <p class="assist-panel">Let our expert compliance team assist you in ensuring that your firm is compliant with all of its money laundering and other compliance obligations.</p>
  <address class="contact contact--back">
    <div class="contact__row"><svg class="contact__icon" viewBox="0 0 10 10"><rect width="10" height="10" fill="#b3131b"/><path d="M2 5l3-3 3 3v3H2z" fill="#fff"/></svg><span>42 W. Halvern Street, Suite 300<br>Pasadena, CA 91101</span></div>
    <div class="contact__gap"></div>
    <div class="contact__row"><svg class="contact__icon" viewBox="0 0 10 10"><rect width="10" height="10" fill="#b3131b"/><path d="M3 2h1.5l.5 2-1 .8a4 4 0 0 0 1.5 1.5l.8-1 2 .5V7.5c0 .4-.4.6-.8.5A6 6 0 0 1 2.5 3c0-.5.1-1 .5-1z" fill="#fff"/></svg><span>(877) 318-4027</span></div>
    <div class="contact__row"><svg class="contact__icon" viewBox="0 0 10 10"><rect width="10" height="10" fill="#b3131b"/><path d="M2 3h6v4H2zM2 3l3 2.2L8 3" fill="none" stroke="#fff" stroke-width=".9"/></svg><span>info@pellridgeandassociates.example</span></div>
    <div class="contact__row"><svg class="contact__icon" viewBox="0 0 10 10"><rect width="10" height="10" fill="#b3131b"/><path d="M3 7l4-4M4.5 3H7v2.5" fill="none" stroke="#fff" stroke-width="1"/></svg><span>www.pellridgeandassociates.example</span></div>
  </address>
  <div class="stamp-box" aria-label="Stamp area"></div>
  <div class="address-lines" aria-label="Mailing address lines"><span></span><span></span><span></span><span></span><span></span></div>
</section>

<section class="postcard postcard--front" aria-label="Postcard front">
  <svg class="front-art" viewBox="0 0 620 438" preserveAspectRatio="none">
    <defs>
      <linearGradient id="cityNight" x1="0" y1="0" x2="1" y2="1">
        <stop offset="0" stop-color="#1f2327"/><stop offset=".55" stop-color="#4a5158"/><stop offset="1" stop-color="#2b3035"/>
      </linearGradient>
      <linearGradient id="wineTone" x1="0" y1="0" x2="0" y2="1">
        <stop offset="0" stop-color="#5a1416"/><stop offset="1" stop-color="#2a0708"/>
      </linearGradient>
      <radialGradient id="chartTone" cx=".45" cy=".4" r=".7">
        <stop offset="0" stop-color="#6f86e0"/><stop offset=".6" stop-color="#3a55c4"/><stop offset="1" stop-color="#16246b"/>
      </radialGradient>
    </defs>
    <g role="img" aria-label="Photograph of a glass office tower at dusk">
      <rect width="620" height="300" fill="url(#cityNight)"/>
    </g>
    <g role="img" aria-label="Dark red photograph of hands with a financial data grid">
      <polygon points="470,0 620,0 620,438 500,438 470,300" fill="url(#wineTone)"/>
    </g>
    <polygon points="0,300 330,300 430,240 500,438 0,438" fill="#ffffff"/>
    <circle cx="455" cy="150" r="128" fill="#9a9c9f" opacity=".55"/>
    <g role="img" aria-label="Close-up photograph of stock market line charts on a screen">
      <circle cx="462" cy="150" r="108" fill="url(#chartTone)"/>
    </g>
  </svg>
  <div class="brand brand--front"><span class="brand__mark"></span>Pellridge &amp; Associates</div>
  <div class="front-copy">
    <h1>Anti-Money Laundering Compliance Services</h1>
    <p>Let our expert compliance team assist you in ensuring that your firm is compliant with all of its money laundering and other compliance obligations.</p>
  </div>
  <address class="contact contact--front">
    <div class="contact__row"><svg class="contact__icon" viewBox="0 0 10 10"><rect width="10" height="10" fill="#b3131b"/><path d="M2 5l3-3 3 3v3H2z" fill="#fff"/></svg><span>42 W. Halvern Street, Suite 300<br>Pasadena, CA 91101</span></div>
    <div class="contact__gap"></div>
    <div class="contact__row"><svg class="contact__icon" viewBox="0 0 10 10"><rect width="10" height="10" fill="#b3131b"/><path d="M3 2h1.5l.5 2-1 .8a4 4 0 0 0 1.5 1.5l.8-1 2 .5V7.5c0 .4-.4.6-.8.5A6 6 0 0 1 2.5 3c0-.5.1-1 .5-1z" fill="#fff"/></svg><span>(877) 318-4027</span></div>
    <div class="contact__row"><svg class="contact__icon" viewBox="0 0 10 10"><rect width="10" height="10" fill="#b3131b"/><path d="M2 3h6v4H2zM2 3l3 2.2L8 3" fill="none" stroke="#fff" stroke-width=".9"/></svg><span>info@pellridgeandassociates.example</span></div>
    <div class="contact__row"><svg class="contact__icon" viewBox="0 0 10 10"><rect width="10" height="10" fill="#b3131b"/><path d="M3 7l4-4M4.5 3H7v2.5" fill="none" stroke="#fff" stroke-width="1"/></svg><span>www.pellridgeandassociates.example</span></div>
  </address>
</section>

</body>
</html>
```